Logo design and Businesscard and letterhead for Technology Company

We need logo design for a new company based in Atlanta called "Vornimel". We provide information about technology Product and service provider companies, information about their Products and services. Our initial focus is to List various companies and their products, various consulting companies and their services. We want to convey the message that this will be one stop shop to find out all the information to make smart technology decisions

I am looking for Logo, Business Card and Letterhead.

Target Market(s)

Companies that have IT department, IT users such as Developers, Managers, C level, Technology Product companies , Consulting companies and service providers.

Industry/Entity Type

It Company

Requirements
Must have
• Looking for some Unique design idea.
Nice to have
• I want something that connects information across technologies between technology buyers and sellers.
Should not have
• No puzzle design.

```html
<!DOCTYPE html>
<html lang="en">
<head>
<meta charset="utf-8">
<title>Vornimel — Logo, Business Card and Letterhead</title>
<link rel="stylesheet" href="https://fonts.googleapis.com/css2?family=Syncopate:wght@400;700&display=swap">
<style>
  :root {
    --orange: #fd5a03;
    --grey: #717171;
    --band-grey: #e0e0e0;
    --paper: #ffffff;
    --page: #ffffff;
    --edge: #d6d6d6;
  }
  * { box-sizing: border-box; margin: 0; padding: 0; }
  html, body {
    width: 771px; height: 1200px; overflow: hidden;
    background: var(--page);
    font-family: "Syncopate", sans-serif;
  }
  .board { position: relative; width: 771px; height: 1200px; }

  .wordmark {
    position: absolute;
    display: flex; align-items: center; gap: 0.3em;
    color: var(--orange);
    font-family: "Syncopate", sans-serif;
    font-weight: 700;
    white-space: nowrap;
  }
  .wordmark .mark-square {
    display: inline-block; width: 0.7em; height: 0.7em;
    background: var(--grey);
  }
  .wordmark--hero { top: 82px; left: 0; width: 771px; justify-content: center; font-size: 52px; }
  .wordmark--letterhead { top: 345px; left: 92px; font-size: 26px; }
  .wordmark--card { top: 537px; left: 404px; font-size: 13px; }

  .letterhead {
    position: absolute; left: 25px; top: 257px; width: 721px; height: 918px;
    background: var(--paper);
    box-shadow: 0 0 18px rgba(0,0,0,0.28);
  }
  .letterhead .band-grey {
    position: absolute; left: 0; right: 0; top: 769px; height: 29px; background: var(--band-grey);
  }
  .letterhead .band-orange {
    position: absolute; left: 0; right: 0; top: 798px; height: 19px; background: var(--orange);
  }

  .contact {
    position: absolute;
    color: var(--grey);
    font-size: 8.6px; line-height: 10.6px; letter-spacing: 1.6px;
    font-weight: 700;
  }
  .contact .contact-name { color: var(--orange); }
  .letterhead-footer { left: 69px; top: 1092px; }

  .business-card {
    position: absolute; left: 376px; top: 508px; width: 307px; height: 175px;
    background: var(--paper);
    border: 1px solid var(--edge);
    border-radius: 6px;
    overflow: hidden;
    box-shadow: 0 0 8px rgba(0,0,0,0.18);
  }
  .business-card .band-grey {
    position: absolute; left: 0; right: 0; top: 136px; height: 19px; background: var(--band-grey);
  }
  .business-card .band-orange {
    position: absolute; left: 0; right: 0; top: 155px; height: 9px; background: var(--orange);
  }
  .card-details { left: 523px; top: 586px; font-size: 8.6px; line-height: 10.4px; }
  .card-details .contact-name { font-size: 11px; line-height: 14px; letter-spacing: 2px; }
</style>
</head>
<body>
  <main class="board">
    <div class="wordmark wordmark--hero"><span class="mark-square"></span>Vornimel</div>

    <section class="letterhead">
      <div class="band-grey"></div>
      <div class="band-orange"></div>
    </section>
    <div class="wordmark wordmark--letterhead"><span class="mark-square"></span>Vornimel</div>

    <address class="contact letterhead-footer" style="font-style:normal">
      <div class="contact-name">Vornimel</div>
      <div>323 Vornimel Rd.</div>
      <div>City, State</div>
      <div>P (123) 456-7891</div>
      <div>F (123) 456-7989</div>
    </address>

    <section class="business-card">
      <div class="band-grey"></div>
      <div class="band-orange"></div>
    </section>
    <div class="wordmark wordmark--card"><span class="mark-square"></span>Vornimel</div>
    <address class="contact card-details" style="font-style:normal">
      <div class="contact-name">John Doe</div>
      <div>323 Vornimel Rd.</div>
      <div>City, State</div>
      <div>P (123) 456-7891</div>
      <div>F (123) 456-7989</div>
    </address>
  </main>
</body>
</html>
```